Kindle Book Cover for Teen Financial Niche

Had a temporary cover done for the book but it needs a lot better cover now it is starting to get some traction.
The current book can be seen here:
https://www.bookvalemart.com/dp/Q7K42LZ9RT
I am wanting something very different if possible. Please search books in the teen financial niche on Bookvale and you will see that a lot of the covers are very similar in style.
I am looking for something different that will stand out in a crowded marketplace.
If you are putting someone on the cover please use a male character rather than a female one.
Thanks
Dale

```html
<!DOCTYPE html>
<html lang="en">
<head>
<meta charset="utf-8">
<title>Personal Finance – Book Cover</title>
<link href="https://fonts.googleapis.com/css2?family=Anton&family=Oswald:wght@500;700&family=Russo+One&display=swap" rel="stylesheet">
<style>
  :root {
    --page: #ffffff;
    --denim-light: #3a5d92;
    --denim-mid: #2a4878;
    --denim-dark: #1a2f55;
    --tan: #d9b47c;
    --tag: #c9a06a;
    --tag-ink: #6a3515;
    --white: #f4f4f4;
    --gold: #f2b52a;
  }
  * { margin: 0; padding: 0; box-sizing: border-box; }
  html, body {
    width: 1200px; height: 1200px; overflow: hidden;
    background: var(--page);
  }
  .canvas { position: relative; width: 1200px; height: 1200px; }
  .cover {
    position: absolute; left: 253px; top: 60px;
    width: 720px; height: 1080px; overflow: hidden;
  }
  .cover-photo {
    position: absolute; inset: 0;
    background:
      radial-gradient(ellipse at 72% 25%, rgba(214,196,160,0.55) 0%, rgba(214,196,160,0.25) 22%, transparent 38%),
      linear-gradient(160deg, var(--denim-light) 0%, var(--denim-mid) 45%, var(--denim-dark) 100%);
  }
  .audience-tag {
    position: absolute; left: 92px; top: 215px;
    width: 205px; height: 300px;
    background: var(--tag);
    border-radius: 14px;
    transform: rotate(-15deg);
    display: flex; flex-direction: column; justify-content: flex-end;
    padding: 0 0 34px 30px;
    font-family: "Oswald", sans-serif; font-weight: 700;
    font-size: 36px; line-height: 1.04; color: var(--tag-ink);
    text-transform: uppercase;
  }
  .tag-hole {
    position: absolute; left: 50%; top: 26px;
    width: 26px; height: 26px; margin-left: -13px;
    border-radius: 50%; background: var(--denim-mid);
  }
  .title {
    position: absolute; left: 0; width: 720px; text-align: center;
    font-family: "Anton", sans-serif; color: var(--tan);
    text-transform: uppercase; line-height: 1; white-space: nowrap;
    font-size: 178px; letter-spacing: 2px;
    transform: scaleX(0.9); transform-origin: center;
  }
  .title-personal { top: 535px; }
  .title-finance { top: 715px; }
  .subtitle {
    position: absolute; left: 0; width: 720px; text-align: center;
    font-family: "Oswald", sans-serif; font-weight: 500;
    color: var(--white); text-transform: uppercase; line-height: 1;
    white-space: nowrap; transform: scaleX(1.3); transform-origin: center;
  }
  .subtitle-lead { top: 896px; font-size: 31px; letter-spacing: 1px; }
  .subtitle-line { font-size: 25px; letter-spacing: 1px; }
  .subtitle-line.one { top: 936px; }
  .subtitle-line.two { top: 968px; }
  .highlight { color: var(--gold); }
  .author {
    position: absolute; left: 0; top: 1018px; width: 720px; text-align: center;
    font-family: "Russo One", sans-serif; font-size: 32px;
    color: var(--white); letter-spacing: 6px; text-transform: uppercase;
    white-space: nowrap; transform: scaleX(1.3); transform-origin: center;
  }
</style>
</head>
<body>
<div class="canvas">
  <div class="cover">
    <div class="cover-photo" role="img" aria-label="Close-up photo of a blue denim jeans front pocket with US dollar bills tucked inside"></div>
    <div class="audience-tag">
      <span class="tag-hole"></span>
      <span>For</span><span>Teens</span><span>and</span><span>Young</span><span>Adults</span>
    </div>
    <h1 class="title title-personal">Personal</h1>
    <div class="title title-finance">Finance</div>
    <p class="subtitle subtitle-lead">Money Mastery</p>
    <p class="subtitle subtitle-line one">A Roadmap to: <span class="highlight">Earning Power</span> Wise</p>
    <p class="subtitle subtitle-line two">Spending <span class="highlight">Budgeting</span> Saving <span class="highlight">Investing</span></p>
    <p class="author">Elias Moreno</p>
  </div>
</div>
</body>
</html>
```